Brane & Hollis LLC
Commercial Real Estate Invesment Group
Brane & Hollis LLC -
Creative Brief
www.braneandhollisllc.example
Fitz & Co.focuses on Undervalued Assets that are cash flowing and have great potential upside.And the elimination of risk.
left side
www.quellmorefunds.example/#/home
www.ridgewaysyndicate.example
www.vantor.example
I need a lot of help here I am of no use visually at all. I do not even know how to answer most of the questions to you
dawnp dawnp
Guys that was the most painful and hard decision I have had to make in a very very long time. Thank you all you are all great and all of your effort was and is greatly appreciated. You are all genuineness and I am a lucky to have had you participate in this.
brightforge brightforge
Hello PH, Please check you PM inbox. Thanks
pixelmonk pixelmonk
Hi PH, Please check your private message. thanks,
Hey to everybody. This going to be a hard selection to be a hard selection process, Everything is great and Thank you for all of you work. I need to talk to support and ask a few questions, that I asked some privately and did not get answers to. I have kept this open because one particular designer asked me to, And I have this other Restaurant thing going on, that has stalled my attention to this. I spent some time doing some time eliminating some just to get a clearer view. I will have pick a winner by Sunday, Thank you all so much
Can Somebody put any thought on the Trelby Hall project please. I am opening that in 3 weeks.
Qv I really like this #29 can you go back to Who we are? Keep the arrow and maybe look for another building for the pic on the right. Fernwright #28 is ok but please re-read the brief and the thread we are a Commercial Real Estate Co.. Can I see it with maybe retail pics, strip centers? Please. Thank you
Lumo 24 & 26 are great 25 a little residential in feel. The path everybody is on is fantastic. A little more about us as a business, we have been investing in Commercial Real Estate as a group for 10 years after moving from Residential we primarily focusing on retail strip centers. We focus of Cash Flow and Dividends return in 1-2 years. And return on Capital by year 5 or sooner. We have a track record of of high returns and not losing money.
LuNaPix7Kw3Fo LuNaPix7Kw3Fo
Hello@dawnp, This is my 1st design hope you like it please feel free to let me know the required changes so that your expectations are met. waiting for your feedback on design#19, #20 & #21 Regrds, LunaPix
Vobe the lay out again is good. The modern building is not working. Thanks
We are US based. Thank you
Vobe4web Vobe4web
Which location are you look at? In US or UK, please advise me further..
And Oh it should be Brane & Hollis LLC is that not on the Logo? And can we try the lettering in the header in black?
I like the layout and concept. But the pic's are residential we need to be looking more retail-City scapeish. Thanks
SiteAdmin SiteAdmin
Logo files have been attached. Kindly see Creative Brief Owen Hartley
pelnoart pelnoart
can u upload your LOGO ?

```html
<!DOCTYPE html>
<html lang="en">
<head>
<meta charset="utf-8">
<title>Brane &amp; Hollis LLC — Commercial Investment Group</title>
<link rel="stylesheet" href="https://fonts.googleapis.com/css2?family=Cinzel:wght@400;700&family=Arimo:wght@400;700&display=swap">
<style>
:root{
  --gold:#e6c57e;
  --gold-light:#f6e1a8;
  --gold-deep:#a9782c;
  --brown-panel:rgba(46,30,12,.88);
  --orange:#f0a43a;
  --ink:#2f2f2f;
  --muted:#555;
  --paper:#f4f2ee;
  --footer:#000;
  --white:#fff;
}
*{box-sizing:border-box;margin:0;padding:0}
html,body{width:1200px;height:857px;overflow:hidden;background:var(--footer)}
body{font-family:Arimo,Arial,sans-serif;color:var(--white)}
.canvas{position:relative;width:1200px;height:857px;overflow:hidden;background:var(--footer)}

.city-photo{position:absolute;left:0;top:0;width:1200px;height:750px;
  background:
    radial-gradient(ellipse 520px 300px at 330px 80px,rgba(255,236,190,.85),transparent 70%),
    linear-gradient(180deg,#b69256 0%,#a47c3e 35%,#7c5a2a 62%,#4a3417 85%,#2a1d0e 100%);}

.brand{position:absolute;left:190px;top:30px;display:flex;align-items:center;gap:14px}
.brand-mark{width:50px;height:50px;background:var(--gold)}
.brand-name{font-family:Cinzel,serif;font-size:32px;font-weight:400;color:var(--gold-light);line-height:1;white-space:nowrap}
.brand-tagline{position:absolute;left:254px;top:72px;font-family:Cinzel,serif;font-size:13px;letter-spacing:1px;color:var(--gold-light);white-space:nowrap}

.contact{position:absolute;left:845px;top:50px}
.contact-phone{display:flex;align-items:center;gap:10px;font-family:Cinzel,serif;font-size:28px;color:var(--white);white-space:nowrap}
.contact-mail{display:flex;align-items:center;gap:10px;margin-top:6px;font-size:14px;color:var(--white);white-space:nowrap}

.tagline-banner{position:absolute;left:552px;top:137px;width:552px;height:46px;background:rgba(35,26,15,.88);
  border:1px solid rgba(255,255,255,.15);display:flex;align-items:center;justify-content:center;
  font-family:Cinzel,serif;font-size:18px;color:var(--white);letter-spacing:.5px;white-space:nowrap}

.main-nav{position:absolute;left:173px;top:140px;width:240px;height:357px;
  background:linear-gradient(180deg,#8d6326,#6e4c1c);border:1px solid #c49a52}
.main-nav ul{list-style:none}
.main-nav li{height:50px;display:flex;align-items:center;gap:12px;padding-left:18px;
  border-bottom:1px solid rgba(255,230,170,.25);font-family:Cinzel,serif;font-size:15px;color:var(--white);white-space:nowrap}
.main-nav li.is-active{background:linear-gradient(180deg,var(--gold-light),var(--gold));color:#4a3210}
.main-nav li::before{content:"";border-left:7px solid currentColor;border-top:5px solid transparent;border-bottom:5px solid transparent}

.news{position:absolute;left:173px;top:497px;width:240px;height:252px;background:var(--brown-panel);padding:14px 16px;font-size:11px;line-height:1.3}
.news-title{font-family:Cinzel,serif;font-size:18px;color:var(--orange);margin-bottom:10px;white-space:nowrap}
.news-item{margin-bottom:9px}
.learn-link{color:var(--orange)}
.news-all{position:absolute;right:16px;bottom:8px;font-family:Cinzel,serif;font-size:11px;color:var(--white)}

.card{position:absolute;top:485px;height:264px;background:var(--paper);color:var(--muted)}
.card-head{height:38px;background:rgba(30,22,12,.92);display:flex;align-items:center;padding-left:12px;
  font-family:Cinzel,serif;font-size:16px;font-weight:400;color:var(--white);white-space:nowrap}
.card-body{padding:10px 12px;font-size:12px;line-height:1.32}
.card-body p+p{margin-top:10px}
.card-more{position:absolute;left:12px;bottom:8px;display:flex;align-items:center;gap:8px;
  font-family:Cinzel,serif;font-size:11px;color:var(--gold-deep)}
.card-more span.dot{width:13px;height:13px;border-radius:50%;background:var(--gold)}
.welcome{left:427px;width:312px}
.opening{left:754px;width:254px}
.opening-photo{position:absolute;left:9px;top:46px;width:236px;height:108px;
  background:linear-gradient(180deg,#7fa3d6 0%,#c8d6ea 55%,#6f8a4a 100%)}
.opening-body{position:absolute;top:160px;left:0;right:0}
.opening-title{font-weight:700;color:var(--ink);font-size:13px;white-space:nowrap}
.opening-title em{font-style:normal;font-weight:400;color:var(--orange);font-size:11px}

.site-footer{position:absolute;left:0;top:770px;width:1200px;text-align:center;font-size:12px;color:var(--white)}
.footer-links{word-spacing:2px}
.footer-copy{margin-top:6px}
.social{display:flex;justify-content:center;gap:6px;margin-top:12px}
.social span{width:18px;height:18px;background:#3b5b9a}
.social span:nth-child(2){background:#33aadd}
.social span:nth-child(3){background:#1d75b3}
.social span:nth-child(4){background:#cc2b2b}
.social span:nth-child(5){background:#e07a1c}
</style>
</head>
<body>
<div class="canvas">
  <div class="city-photo" role="img" aria-label="Sepia photograph of a downtown city skyline with high-rise office towers"></div>

  <div class="brand"><span class="brand-mark"></span><span class="brand-name">Brane &amp; Hollis LLC</span></div>
  <div class="brand-tagline">Commercial Investment Group</div>

  <div class="contact">
    <div class="contact-phone">
      <svg width="22" height="22" viewBox="0 0 24 24" aria-hidden="true"><path fill="#fff" d="M6.6 10.8a15 15 0 0 0 6.6 6.6l2.2-2.2c.3-.3.7-.4 1-.2 1.1.4 2.3.6 3.6.6.6 0 1 .4 1 1V20c0 .6-.4 1-1 1C10.6 21 3 13.4 3 4c0-.6.4-1 1-1h3.5c.6 0 1 .4 1 1 0 1.3.2 2.5.6 3.6.1.3 0 .7-.2 1z"/></svg>
      000 000 1234
    </div>
    <div class="contact-mail">
      <svg width="20" height="14" viewBox="0 0 20 14" aria-hidden="true"><rect x="0.5" y="0.5" width="19" height="13" fill="#fff"/><path d="M1 1l9 7 9-7" fill="none" stroke="#7c5a2a" stroke-width="1.4"/></svg>
      contact@braneandhollisllc.example
    </div>
  </div>

  <div class="tagline-banner">Commercial Real Estate Invesment Group</div>

  <nav class="main-nav">
    <ul>
      <li class="is-active">Home</li>
      <li>Who we are?</li>
      <li>Our portfolio</li>
      <li>What we invest in</li>
      <li>In the media</li>
      <li>Testimonials</li>
      <li>Contact Us</li>
    </ul>
  </nav>

  <aside class="news">
    <h2 class="news-title">News &amp; Updates</h2>
    <div class="news-item">
      <div>13.06.2011</div>
      <div>Brane &amp; Hollis LLC International Hotel &amp; Tower Chicago Awarded World's Best Service Honor by Voyage &amp; Ease</div>
      <div class="learn-link">Learn more</div>
    </div>
    <div class="news-item">
      <div>13.06.2011</div>
      <div>Brane &amp; Hollis LLC International Hotel &amp; Tower Chicago Awarded World's Best Service Honor by Voyage &amp; Ease</div>
      <div class="learn-link">Learn more</div>
    </div>
    <div class="news-all">View all</div>
  </aside>

  <section class="card welcome">
    <h2 class="card-head">Welcome to Brane &amp; Hollis LLC</h2>
    <div class="card-body">
      <p>Lorem ipsum dolor sit amet, consectetur adipiscing elit. Suspendisse sed nibh nec dui luctus sollicitudin. Mauris consequat mi pharetra ligula pellentesque eu rutrum erat pellentesque. Donec lectus erat, lobortis et condimentum dignissim, porta in sapien.</p>
      <p>Vivamus tellus mauris, fringilla eu tempus nec, tincidunt in mi. Donec iaculis rutrum tortor ut tempor. Nunc id nibh in est commodo pulvinar. Maecenas quis elit tincidunt arcu consectetur consequat ut sed risus.</p>
    </div>
    <div class="card-more"><span class="dot"></span>Learn more</div>
  </section>

  <section class="card opening">
    <h2 class="card-head">Current Opening</h2>
    <div class="opening-photo" role="img" aria-label="Photograph of the featured property building"></div>
    <div class="card-body opening-body">
      <div class="opening-title">Trelby Hall project - <em>11 July 2011</em></div>
      <p>Lorem ipsum dolor sit amet, consectetur adipiscing elit. Suspendisse sed nibh nec dui.</p>
    </div>
    <div class="card-more"><span class="dot"></span>Learn more</div>
  </section>

  <footer class="site-footer">
    <div class="footer-links">Home &nbsp;|&nbsp; Who we are &nbsp;|&nbsp; Our portfolio &nbsp;|&nbsp; What we invest in &nbsp;|&nbsp; In the media &nbsp;|&nbsp; Testimonials &nbsp;|&nbsp; Contact Us</div>
    <div class="footer-copy">Copyright © 2011, Brane &amp; Hollis LLC. All rights reserved.</div>
    <div class="social" aria-label="Social links"><span></span><span></span><span></span><span></span><span></span></div>
  </footer>
</div>
</body>
</html>
```